Quillory Nest Business Card

I need a business card design. We are a collaborate online training company. Our colors are gray and green. Our website is QuilloryNest.com

I would like an area for a profile picture within the card

```html
<!DOCTYPE html>
<html lang="en">
<head>
<meta charset="utf-8">
<title>Quillory Nest Business Card</title>
<link rel="stylesheet" href="https://fonts.googleapis.com/css2?family=PT+Sans+Narrow:wght@400;700&display=swap">
<style>
  :root {
    --green: #8cc540;
    --green-light: #d8ecb8;
    --black: #000000;
    --panel-dark: #6a6260;
    --gray: #bdbec2;
    --gray-light: #eeeeef;
    --white: #ffffff;
    --ink: #111111;
  }
  html, body {
    margin: 0;
    padding: 0;
    width: 1010px;
    height: 1200px;
    overflow: hidden;
    background: var(--white);
    font-family: "PT Sans Narrow", sans-serif;
  }
  .canvas {
    position: relative;
    width: 1010px;
    height: 1200px;
    overflow: hidden;
  }

  /* Front side */
  .card-front {
    position: absolute;
    left: 0; top: 0;
    width: 1010px; height: 588px;
    background: var(--green);
  }
  .front-band {
    position: absolute;
    left: 0; top: 118px;
    width: 1010px; height: 351px;
    background: var(--black);
  }
  .brand {
    position: absolute;
    left: 252px; top: 232px;
    display: flex;
    align-items: center;
    gap: 22px;
  }
  .brand-dot {
    width: 74px; height: 74px;
    border-radius: 50%;
    background: var(--green);
  }
  .brand-name {
    color: var(--white);
    font-weight: 700;
    font-size: 84px;
    line-height: 1;
    letter-spacing: -1px;
  }

  /* Back side */
  .card-back {
    position: absolute;
    left: 0; top: 608px;
    width: 1010px; height: 592px;
    background: var(--green);
    overflow: hidden;
  }
  .back-accent {
    position: absolute;
    left: 843px; top: 0;
    width: 167px; height: 592px;
    background: radial-gradient(circle at 60% 85%, var(--green-light) 0%, var(--green) 45%);
  }
  .photo-panel {
    position: absolute;
    left: 77px; top: 0;
    width: 276px; height: 592px;
    background: radial-gradient(circle at 40% 22%, var(--panel-dark) 0%, #2a2625 30%, var(--black) 60%);
  }
  .profile-picture {
    position: absolute;
    left: 0; top: 92px;
    width: 319px; height: 500px;
    background: var(--white);
    border-radius: 70px 70px 0 0;
  }
  .profile-label {
    position: absolute;
    left: 92px; top: 372px;
    width: 120px;
    text-align: center;
    font-size: 36px;
    line-height: 1.2;
    color: var(--ink);
    font-weight: 400;
  }
  .info-panel {
    position: absolute;
    left: 353px; top: 0;
    width: 490px; height: 592px;
    background: radial-gradient(circle at 82% 72%, var(--gray-light) 0%, var(--gray) 35%);
  }
  .person-name {
    position: absolute;
    left: 24px; top: 50px;
    margin: 0;
    font-size: 86px;
    font-weight: 400;
    line-height: 1;
    color: var(--ink);
    letter-spacing: -1px;
  }
  .person-title {
    position: absolute;
    left: 32px; top: 146px;
    margin: 0;
    font-size: 27px;
    color: var(--ink);
  }
  .contact-list {
    position: absolute;
    left: 20px; top: 354px;
    margin: 0; padding: 0;
    list-style: none;
  }
  .contact-item {
    display: flex;
    align-items: center;
    height: 47px;
    font-size: 32px;
    color: var(--ink);
  }
  .contact-icon {
    width: 38px; height: 34px;
    margin-right: 17px;
    flex: none;
  }
</style>
</head>
<body>
<div class="canvas">

  <section class="card-front">
    <div class="front-band">
      <div class="brand" style="top:114px;">
        <span class="brand-dot"></span>
        <span class="brand-name">QuilloryNest</span>
      </div>
    </div>
  </section>

  <section class="card-back">
    <div class="photo-panel"></div>
    <div class="profile-picture" role="img" aria-label="Profile photo of the card holder"></div>
    <div class="profile-label">profile picture</div>

    <div class="info-panel">
      <h1 class="person-name">mara kessling</h1>
      <p class="person-title">title</p>
      <ul class="contact-list">
        <li class="contact-item">
          <svg class="contact-icon" viewBox="0 0 38 34"><circle cx="19" cy="17" r="14" fill="#111"/></svg>
          @socialaccount
        </li>
        <li class="contact-item">
          <svg class="contact-icon" viewBox="0 0 38 34"><rect x="11" y="3" width="16" height="29" rx="3" fill="#111"/><rect x="14" y="8" width="10" height="10" fill="#bdbec2"/><rect x="16" y="22" width="6" height="6" rx="1" fill="#bdbec2"/></svg>
          555.123.4567
        </li>
        <li class="contact-item">
          <svg class="contact-icon" viewBox="0 0 38 34"><rect x="6" y="8" width="26" height="18" fill="none" stroke="#111" stroke-width="3"/><path d="M6 9 L19 19 L32 9" fill="none" stroke="#111" stroke-width="3"/></svg>
          youremail@emailaddress.com
        </li>
        <li class="contact-item">
          <svg class="contact-icon" viewBox="0 0 38 34"><circle cx="17" cy="16" r="13" fill="none" stroke="#111" stroke-width="3"/><ellipse cx="17" cy="16" rx="5" ry="13" fill="none" stroke="#111" stroke-width="2.5"/><path d="M4 16 H30 M6 9 H28 M6 23 H28" stroke="#111" stroke-width="2.5"/><path d="M22 18 L34 24 L28 26 L31 32 L28 33 L25 27 L22 31 Z" fill="#111" stroke="#bdbec2" stroke-width="1"/></svg>
          www.quillorynest.com
        </li>
      </ul>
    </div>

    <div class="back-accent"></div>
  </section>

</div>
</body>
</html>
```